Re-design existing website and add products for sale.

Our current website is very basic and cluttered. (emberfernwellness.com.au)We want a modern looking website that is easy to navigate. We also want to start selling essential oils and crystal products, so there needs to be a separate page for this. Also needs to be easily edited as we need to change the monthly oracle card with the description. Would like calming colours as we are all about natural healing. Alongside the services listed there should be a button to book now which asks for their name, email, phone number ect. and adds it to the cart.

• Logo is still being designed, please leave a space for the logo which will basically be a lotus flower within a mandala.

```html
<!DOCTYPE html>
<html lang="en">
<head>
<meta charset="utf-8">
<title>Ember Fern Wellness – About</title>
<link rel="stylesheet" href="https://fonts.googleapis.com/css2?family=Gabriela&family=Overlock:ital,wght@0,400;0,700;1,400;1,700&family=Open+Sans:wght@700;800&display=swap">
<style>
  :root {
    --page: #fefeec;
    --gold: #d1913a;
    --ink: #111111;
    --card: rgba(255, 255, 255, 0.82);
    --watermark: rgba(214, 160, 90, 0.18);
    --ornament: #1a1a1a;
  }
  * { box-sizing: border-box; margin: 0; padding: 0; }
  html, body { width: 1200px; height: 1000px; overflow: hidden; }
  body {
    position: relative;
    background: var(--page);
    color: var(--ink);
    font-family: "Overlock", sans-serif;
  }
  .backdrop-decoration {
    position: absolute;
    left: 160px; top: 370px;
    width: 880px; height: 630px;
    background: radial-gradient(ellipse at 50% 55%, var(--watermark) 0%, rgba(214,160,90,0.10) 55%, rgba(214,160,90,0) 75%);
  }
  .site-nav {
    position: absolute;
    top: 30px; left: 110px;
    width: 980px; height: 30px;
  }
  .nav-link {
    position: absolute;
    top: 0; width: 192px; height: 30px;
    background: var(--gold);
    color: #fff;
    font-family: "Open Sans", sans-serif;
    font-weight: 700;
    font-size: 18px;
    line-height: 30px;
    text-align: center;
    text-decoration: none;
  }
  .nav-home { left: 0; }
  .nav-services { left: 198px; }
  .nav-about { left: 590px; }
  .nav-contact { left: 788px; }
  .logo-space {
    position: absolute;
    left: 400px; top: -12px; width: 180px;
    text-align: center;
    font-family: "Open Sans", sans-serif;
    font-weight: 700;
    font-size: 44px;
    line-height: 56px;
  }
  .hero {
    position: absolute;
    top: 132px; left: 0; width: 1200px;
    text-align: center;
    font-family: "Gabriela", serif;
  }
  .hero-title {
    font-size: 64px; font-weight: 400; line-height: 80px;
    transform: scaleX(0.9);
  }
  .hero-tagline {
    font-size: 33px; font-weight: 400; line-height: 44px; margin-top: -2px;
    transform: scaleX(0.82);
  }
  .about-card {
    position: absolute;
    left: 140px; top: 285px;
    width: 920px; height: 455px;
    background: var(--card);
    box-shadow: 0 2px 5px rgba(0,0,0,0.18);
    padding: 22px 20px 0;
  }
  .about-heading {
    display: flex;
    justify-content: center;
    align-items: center;
    gap: 16px;
    font-size: 34px;
    font-weight: 400;
    letter-spacing: 0.6px;
    line-height: 40px;
    margin-bottom: 18px;
  }
  .heading-ornament {
    display: block;
    width: 32px; height: 30px;
    border-radius: 50%;
    background: var(--ornament);
  }
  .about-text p {
    font-style: italic;
    font-size: 21px;
    letter-spacing: 0.45px;
    line-height: 23px;
    margin-bottom: 23px;
  }
  .lineage-card {
    position: absolute;
    left: 140px; top: 769px;
    width: 445px; height: 260px;
    background: var(--card);
    box-shadow: 0 2px 5px rgba(0,0,0,0.18);
    padding-top: 16px;
    text-align: center;
    font-style: italic;
    font-size: 21px;
    letter-spacing: 0.3px;
    line-height: 23px;
  }
  .lineage-title { font-size: 20px; font-weight: 700; letter-spacing: -0.2px; }
  .lineage-list { list-style: none; }
  .studio-photo {
    position: absolute;
    left: 615px; top: 769px;
    width: 445px; height: 231px;
    background: linear-gradient(100deg, #cfcfcf 0%, #9a9a9a 45%, #5e5e5e 100%);
  }
</style>
</head>
<body>
  <div class="backdrop-decoration" role="img" aria-label="Faint decorative lotus mandala in pale gold behind the content"></div>

  <nav class="site-nav">
    <a class="nav-link nav-home" href="#">HOME</a>
    <a class="nav-link nav-services" href="#">SERVICES</a>
    <div class="logo-space">LOGO</div>
    <a class="nav-link nav-about" href="#">ABOUT</a>
    <a class="nav-link nav-contact" href="#">CONTACT</a>
  </nav>

  <header class="hero">
    <h1 class="hero-title">Ember Fern Wellness</h1>
    <p class="hero-tagline">Find Your True Self &amp; Bring Balance To Your Life</p>
  </header>

  <section class="about-card">
    <h2 class="about-heading">
      <span class="heading-ornament" role="img" aria-label="Small lotus ornament"></span>
      About Clara Vennings
      <span class="heading-ornament" role="img" aria-label="Small lotus ornament"></span>
    </h2>
    <div class="about-text">
      <p>My love of all things spiritual and holistic started as a young girl and deepened when I first studied Reiki 19 years ago in 2000.</p>
      <p>After suffering with a hereditary medical problem from early childhood, I set about finding a solution in conjunction with modern medicine, which would enable me to get through each day both calmer and stronger, while feeling more vibrant and alive.</p>
      <p>It was not until 2016 however, that I finally realised I wanted to use my training and abilities to help the wider community, rather than just those close to me. With that in mind, I set about gaining my Reiki Master/Teacher and Seichim Master/Teacher qualifications to not only help those requiring healing, but to further spread the joy of Reiki and Seichim and teach those who wish to learn these wonderful healing techniques.</p>
      <p>Now years later, as an initiated Reiki &amp; Seichim Master/Teacher I'm here to provide you with intuitive healing to help balance your body, mind and spirit.</p>
    </div>
  </section>

  <section class="lineage-card">
    <h3 class="lineage-title">Hikari Shiki Ryoho Lineage Of Masters</h3>
    <ul class="lineage-list">
      <li>Dr Kenji Arimoto</li>
      <li>Dr Tadao Moriyama</li>
      <li>Emiko Tanabe</li>
      <li>Lorna Mei Kawahara</li>
      <li>Greta Lindqvist</li>
      <li>Harper Dunmore</li>
      <li>Ben &amp; Ruth Calder</li>
      <li>Jan &amp; Colin Pryor</li>
      <li>Marion Coletti</li>
    </ul>
  </section>

  <div class="studio-photo" role="img" aria-label="Black and white photo of the healing room with wall hangings, shelves and a treatment table"></div>
</body>
</html>
```